依頼詳細
ラックに並べられた時に見えるよう(雑誌のように)タイトルは上部にお願いします。写真を大きめに使ってください。美しい音で心に深くしみわたるような演奏にしたいと思っています。やさしく透明感のあるイメージでお願いします。
記載項目
森川沙織ピアノリサイタル
2014年11月8日(土)/開演18:00(開場17:30)
ソラノ心斎橋音楽サロン゛Brise”(大阪駅前第3ビル1F)
入場料(全自由席)前売:3000円 当日3500円 *未就学児の入場はごご遠慮くださいチケット販売 t* ティーナビ(サンデイストア Sunaターミナル)
お問い合わせ ソラノ心斎橋 大阪市北区曽根崎4丁目7番2(大阪駅前第3ビル1F)Tel. 06-6921-4057 , http://saorimori-piano.example/
後援 浪華音楽学院同窓会《響友会》、近畿鍵盤文化協会/
Program (原語表記のものを添付させていただきました)
モーツァルト/ソナタ第10番ハ長調 K.330
ラヴェル/ソナチネ
ラヴェル/「鏡」より 道化師の朝の歌
シューマン/交響的練習曲Op.13
Profile (添付させていただきました)
サイズ
A4
ページ数
片面
希望イメージ
シンプル 複雑
単色 カラフル
暗い 明るい
日常 高級
遊び心 厳粛
未来的 伝統的
女性的 男性的
希望する色
設定なし
納品ファイル
• イラストレーター形式 (.ai)
• フォトショップ形式 (.psd)
補足説明
写真を3枚添付していますが、どれか1枚を選んで使ってください。写真はイメージに合うようにカットしたり加工してくださって結構です。プログラムも添付しましたが、原語表記なしの日本語表記のみでも結構です。ナチュラルなイメージが希望です。
写真をもう一度添付してみました。
たびたび申し訳ありません。
プロフィール、並びに プログラムのファイルも添付できていなかったようなので、そちらももう一度添付します。
よろしくお願いいたします。
数々のご提案ありがとうございます。
みなさんとてもステキなのですが、私の好みを補足させていただきます。

顔以外のスペースが文字で埋まってしまうのは好きではありません。
「間」というのか、「抜け感」というのでしょうか…適度なスペースがほしいです。
音楽も「音と音のあいだに音楽が存在する」ものです。
こんな写真で申し訳ありませんが、ぜひアーティストとしてのセンス、インスピレーションを発揮してください☆よろしくお願いいたします。
■ 選んだ理由

私が表現したい音のイメージと合っているように思いました。
光のキラキラとしたようなものが入っていて、それが音のキラキラに通じるように思ったのと、透明感が感じられ、また柔らかい雰囲気もあると思います。
それなのに、チラシを見たときの印象が強いので、この提案に決めました。

■ 提案者全員のお礼・コメント

たくさんのご提案ありがとうございました。みなさんとてもステキなので、当選&次点を選ぶのが失礼なくらいでした。自分で考えるようなものとは全く違って、さすがプロのお仕事だなぁと思いました。多くのワガママを聞き入れてくださり、本当にありがとうございました。またお願いしたいと思います。感謝申し上げます。

```html
<!DOCTYPE html>
<html lang="ja">
<head>
<meta charset="utf-8">
<title>森川沙織 ピアノリサイタル</title>
<link rel="stylesheet" href="https://fonts.googleapis.com/css2?family=Noto+Serif+JP:wght@400;600&family=Noto+Sans+JP:wght@400;500;700&family=Great+Vibes&display=swap">
<style>
:root{
  --red:#b5202c;
  --red-deep:#9c1822;
  --ink:#3a3434;
  --soft:#6c6464;
  --wall-a:#f7f6f4;
  --wall-b:#e9e7e3;
  --white:#ffffff;
}
*{box-sizing:border-box;margin:0;padding:0}
html,body{width:846px;height:1200px;overflow:hidden;background:#fff}
.flyer{position:relative;width:846px;height:1200px;overflow:hidden;
  background:linear-gradient(160deg,var(--wall-a),var(--wall-b));
  font-family:"Noto Sans JP",sans-serif;color:var(--ink)}
.wall{position:absolute;inset:0 0 95px 0;background:radial-gradient(ellipse at 65% 35%,#fff 0%,rgba(255,255,255,0) 70%)}
.portrait{position:absolute;left:0;top:0;width:360px;height:600px;
  background:linear-gradient(180deg,#f1ece8 0%,#e6d3c6 35%,#d9b9a8 55%,#c0393f 78%,rgba(190,50,58,0) 100%);
  -webkit-mask-image:linear-gradient(90deg,#000 70%,transparent 100%);
  mask-image:linear-gradient(90deg,#000 70%,transparent 100%)}
.title{position:absolute;left:410px;top:70px;color:var(--red);font-family:"Noto Serif JP",serif}
.title .name{font-size:66px;font-weight:600;letter-spacing:.08em;line-height:1}
.title .kind{font-size:42px;font-weight:400;letter-spacing:.06em;margin-top:28px;line-height:1}
.script{font-family:"Great Vibes",cursive;color:var(--red);font-size:30px;line-height:1}
.program{position:absolute;left:420px;top:345px;width:390px}
.program .script{text-align:right;border-bottom:1px solid var(--red);padding-bottom:4px;margin-bottom:12px}
.piece{padding:5px 0 7px;border-bottom:1px dotted #b9b1ae}
.piece .ja{font-size:15px;letter-spacing:.02em}
.piece .orig{font-size:9px;color:var(--soft)}
.date{position:absolute;left:418px;top:575px;color:var(--red);font-family:"Noto Serif JP",serif}
.date .big{font-size:58px;font-weight:600;letter-spacing:.01em;line-height:1}
.date .big small{font-size:30px}
.date .time{font-size:14px;color:var(--ink);margin-top:6px;font-family:"Noto Sans JP",sans-serif}
.venue{position:absolute;left:430px;top:660px;font-size:20px;font-weight:700;color:var(--red);letter-spacing:.03em}
.prices{position:absolute;left:440px;top:705px;display:flex;gap:10px}
.price-table{border-collapse:collapse}
.price-table td{border:1px solid var(--red);padding:3px 14px;font-size:15px}
.price-table .label{background:var(--red);color:#fff;font-size:13px}
.price-table .amount{font-size:22px;font-weight:700;letter-spacing:.02em}
.free{width:54px;background:var(--red);color:#fff;font-size:14px;font-weight:700;display:flex;align-items:center;justify-content:center;text-align:center;line-height:1.3}
.notes{position:absolute;left:440px;top:790px;width:380px;font-size:11.5px;line-height:1.6}
.notes .mark{color:var(--red)}
.notes p+p{margin-top:8px}
.profile{position:absolute;left:38px;top:690px;width:360px}
.profile .script{font-size:28px;margin-bottom:6px}
.profile .who{font-size:13px;font-weight:500;margin-bottom:6px}
.profile .body{font-size:9.6px;line-height:1.75;color:var(--ink);text-align:justify}
.profile .body p+p{margin-top:6px}
.footer{position:absolute;left:0;bottom:0;width:846px;height:95px;background:var(--red-deep);color:#fff;padding:10px 30px;display:flex;justify-content:space-between}
.footer .info{font-size:10.5px;line-height:1.55}
.footer .info strong{font-size:14px;font-weight:700;display:block}
.access{display:flex;gap:10px;align-items:flex-start}
.access .text{font-size:9.5px;line-height:1.5;width:160px}
.map{width:150px;height:75px;background:linear-gradient(135deg,#fbf7f6,#ece4e2)}
</style>
</head>
<body>
<main class="flyer">
  <div class="wall"></div>
  <div class="portrait" role="img" aria-label="ピアニスト森川沙織のポートレート写真(赤いトップス、明るい光)"></div>

  <header class="title">
    <h1 class="name">森川沙織</h1>
    <p class="kind">ピアノリサイタル</p>
  </header>

  <section class="program">
    <div class="script">Program</div>
    <div class="piece"><div class="ja">モーツァルト／ソナタ第10番ハ長調　K.330</div><div class="orig">W.A.Mozart / Sonate No.10 C-dur K.330</div></div>
    <div class="piece"><div class="ja">ラヴェル／ソナチネ</div><div class="orig">M.Ravel / Sonatine</div></div>
    <div class="piece"><div class="ja">ラヴェル／「鏡」より　道化師の朝の歌</div><div class="orig">M.Ravel / Miroirs "Alborada del gracioso"</div></div>
    <div class="piece"><div class="ja">シューマン／交響的練習曲 Op.13</div><div class="orig">R.Schumann / Etudes symphoniques Op.13</div></div>
  </section>

  <section class="date">
    <div class="big">2014.11.8<small>(土)</small></div>
    <div class="time">開演18:00（開場17:30）</div>
  </section>
  <div class="venue">ソラノ心斎橋音楽サロン゛Brise”</div>

  <div class="prices">
    <table class="price-table">
      <tr><td class="label">前売</td><td class="amount">3,000円</td></tr>
      <tr><td class="label">当日</td><td class="amount">3,500円</td></tr>
    </table>
    <div class="free">全席<br>自由</div>
  </div>

  <section class="notes">
    <p>※未就学児の入場はご遠慮ください</p>
    <p><span class="mark">●</span>チケット販売<br>　t* ティーナビ（サンデイストア Sunaターミナル）</p>
    <p><span class="mark">●</span>お問い合わせ<br>　ソラノ心斎橋　Tel. 06-6921-4057</p>
  </section>

  <section class="profile">
    <div class="script">Profile</div>
    <div class="who">森川沙織（Saori Morikawa）</div>
    <div class="body">
      <p>大阪府出身。浪華音楽学院ピアノ科卒業。在学中より数々の演奏会に出演し、卒業後はソロ・室内楽の両面で活動を広げる。これまでにピアノを複数の師に学び、国内外の講習会にて研鑽を積む。</p>
      <p>コンクールにて入賞を重ね、各地でのリサイタルや学校公演、ホールでのアンサンブル公演に出演。やわらかく透明感のある音色と、丁寧な音楽づくりに定評がある。</p>
      <p>現在、後進の指導にあたるとともに、地域のサロンコンサートを主宰。浪華音楽学院同窓会《響友会》会員、近畿鍵盤文化協会会員。</p>
      <p>http://saorimori-piano.example/</p>
    </div>
  </section>

  <footer class="footer">
    <div class="info">
      <strong>ソラノ心斎橋音楽サロン゛Brise”</strong>
      大阪市北区曽根崎4丁目7番2（浪速中央第5ビル1F）<br>
      http://saorimori-piano.example/<br>
      後援　浪華音楽学院同窓会《響友会》／近畿鍵盤文化協会
    </div>
    <div class="access">
      <div class="text"><strong>●アクセス</strong><br>各線「梅田」駅より徒歩約5分<br>浪速中央第5ビル1F</div>
      <div class="map" role="img" aria-label="会場周辺の案内地図"></div>
    </div>
  </footer>
</main>
</body>
</html>
```